I am currently the State's Attorney in a moderately sized county and will have an election in 2020. I need a design for signs and T-shirts. I'd like it very simple but somewhat distinctive if possible. My name is Ray Tollen. All I really need on any sign or t-shirt is TOLLEN and State's Attorney. I'm wondering if there is a way to put the Ray vertically by the K, then have TOLLEN significantly pronounced and then State's Attorney under that. I'd also wonder if there is any way to incorporate the scales of justice, possibly in the two LL('s) in TOLLEN. I can email the former State's Attorney's signs and also some other county wide elected officials' signs so you can see what others do. So you will see three different signs in my county, one by the State's Attorney I replaced. I like the simple design. State's Attorney has to be on the design but should likely be less prominently displayed than my name. Again, I don't know if the scales of justice can work into the two LL's in my name but if they could, that would be both unique and hopefully appropriate. I'm not necessarily tied to color scheme either. Reds and Blues seem to be what folks use. Email me with any questions at rjtollensr@quorvex.net Thanks.

```html
<!DOCTYPE html>
<html lang="en">
<head>
<meta charset="utf-8">
<title>Ray Tollen — State's Attorney</title>
<link rel="stylesheet" href="https://fonts.googleapis.com/css2?family=EB+Garamond:ital,wght@0,700;1,700&display=swap">
<style>
  :root {
    --sign-blue: #214fa3;
    --sign-red: #ed1c24;
    --sign-white: #ffffff;
    --page-bg: #ffffff;
  }
  html, body {
    margin: 0;
    padding: 0;
    width: 1200px;
    height: 900px;
    overflow: hidden;
    background: var(--page-bg);
  }
  .campaign-sign {
    display: block;
    width: 1200px;
    height: 900px;
  }
  .name-panel { fill: var(--sign-blue); }
  .office-band { fill: var(--sign-red); }
  .inner-frame {
    fill: none;
    stroke: var(--sign-white);
    stroke-width: 6;
  }
  .first-name,
  .last-name {
    font-family: "EB Garamond", Garamond, Georgia, serif;
    font-weight: 700;
    fill: var(--sign-white);
  }
  .first-name { font-size: 206px; }
  .last-name { font-size: 306px; }
  .office-title {
    font-family: "EB Garamond", Garamond, Georgia, serif;
    font-style: italic;
    font-weight: 700;
    font-size: 150px;
    fill: var(--sign-white);
  }
</style>
</head>
<body>
  <svg class="campaign-sign" viewBox="0 0 1200 900" xmlns="http://www.w3.org/2000/svg" role="img" aria-label="Ray Tollen, State's Attorney">
    <rect class="name-panel" x="31" y="74" width="1135" height="523"/>
    <path class="inner-frame" d="M57 597 V101 H1142.5 V597"/>
    <rect class="office-band" x="31" y="597" width="1135" height="228"/>

    <text class="first-name" x="123" y="278">Ray</text>
    <text class="last-name" x="116" y="543" textLength="977" lengthAdjust="spacingAndGlyphs">TOLLEN</text>
    <text class="office-title" x="157" y="740" textLength="890" lengthAdjust="spacingAndGlyphs">State's Attorney</text>
  </svg>
</body>
</html>
```